Re design my company logo boost my identity

Hello ,

i am asking for redesign and editing my logo to design a stationery for me
please don't ask many question just let your creativity kicks off .

don't change the logo 360 degree just boost it
my main color is Blue Light please be sure this color appear in your design very well
Blue Light = PANTONE 13-4909

Target Market(s)

young mens and girls 14 to 36 year old

Industry/Entity Type

It Company

Requirements
Must have
• my main color is Blue Light please be sure this color appear in your design very well
• Blue Light = PANTONE 13-4909

```html
<!DOCTYPE html>
<html lang="en">
<head>
<meta charset="utf-8">
<title>Haloware Stationery</title>
<link href="https://fonts.googleapis.com/css2?family=Montserrat:wght@400;500;600&family=Arimo:wght@400;700&display=swap" rel="stylesheet">
<style>
  :root {
    --blue-light: #5bc8dc;
    --ink: #2f2f33;
    --halo: #c98a1e;
    --paper: #ffffff;
    --stage: #ececec;
    --text: #3a3a3a;
    --edge: #d6d6d6;
  }
  * { box-sizing: border-box; margin: 0; padding: 0; }
  html, body { width: 1200px; height: 937px; overflow: hidden; }
  body { background: var(--stage); position: relative; font-family: "Arimo", Arial, sans-serif; color: var(--text); }

  .piece { position: absolute; background: var(--paper); border: 1px solid var(--edge); overflow: hidden; }
  .band { position: absolute; left: 0; bottom: 0; width: 100%; background: linear-gradient(175deg, var(--ink) 0%, #3f6f7a 30%, var(--blue-light) 60%); }

  .brand { position: absolute; display: flex; align-items: center; gap: 0.35em; font-family: "Montserrat", sans-serif; font-weight: 500; color: var(--blue-light); letter-spacing: 0.02em; line-height: 1; }
  .brand-dot { width: 0.42em; height: 0.42em; border-radius: 50%; background: var(--halo); flex: none; }

  .site { position: absolute; font-family: "Montserrat", sans-serif; letter-spacing: 0.22em; color: var(--ink); z-index: 2; }

  /* Letterhead */
  .letterhead { left: 184px; top: 66px; width: 388px; height: 546px; }
  .letterhead .brand { left: 34px; top: 36px; font-size: 26px; }
  .contact-list { position: absolute; right: 26px; top: 24px; list-style: none; font-size: 4.6px; line-height: 8px; text-align: right; }
  .contact-list li { display: flex; justify-content: flex-end; align-items: center; gap: 3px; }
  .contact-list li::after { content: ""; width: 5px; height: 5px; border-radius: 50%; background: var(--halo); }
  .letter { position: absolute; left: 36px; top: 138px; width: 300px; font-size: 5.4px; line-height: 8px; }
  .letter p { margin-bottom: 8px; }
  .letter .gap { margin-bottom: 22px; }
  .letter strong { font-weight: 700; }
  .signature-line { width: 26px; height: 14px; border-bottom: 1px solid var(--text); margin: 4px 0 6px; }
  .letterhead .band { height: 80px; }

  /* Folder */
  .folder { left: 635px; top: 40px; width: 459px; height: 578px; }
  .folder .brand { left: 0; right: 0; top: 250px; justify-content: center; font-size: 64px; }
  .folder .band { height: 100px; }
  .folder .site { right: 22px; bottom: 14px; font-size: 11px; color: #fff; }

  /* Business cards */
  .card { left: 45px; width: 177px; height: 100px; border-radius: 8px; }
  .card-front { top: 658px; }
  .card-front .brand { left: 12px; top: 14px; font-size: 15px; }
  .card-front .band { height: 42px; }
  .holder { position: absolute; left: 14px; top: 40px; font-size: 4.8px; line-height: 6px; }
  .holder .name { color: var(--halo); font-weight: 700; text-transform: uppercase; }
  .card-contacts { position: absolute; left: 96px; top: 64px; list-style: none; font-size: 3.6px; line-height: 5.4px; color: #fff; z-index: 2; }
  .card-contacts li::before { content: ""; display: inline-block; width: 3.6px; height: 3.6px; border-radius: 50%; background: #fff; margin-right: 3px; vertical-align: middle; }
  .card-back { top: 785px; }
  .card-back .brand { left: 0; right: 0; top: 38px; justify-content: center; font-size: 20px; }

  /* Envelopes */
  .envelope-front { left: 264px; top: 672px; width: 433px; height: 209px; }
  .envelope-front .brand { left: 36px; top: 24px; font-size: 24px; }
  .envelope-front .band { height: 100px; }
  .envelope-front .site { right: 26px; bottom: 12px; font-size: 9px; color: #fff; }
  .envelope-back { left: 737px; top: 672px; width: 397px; height: 207px; }
  .flap { position: absolute; left: 0; top: 0; width: 100%; height: 72px; background: var(--blue-light); border-radius: 0 0 48px 48px; }
  .envelope-back .site { left: 0; right: 0; top: 30px; text-align: center; font-size: 12px; }
</style>
</head>
<body>

<section class="piece letterhead">
  <div class="brand"><span class="brand-dot"></span>Haloware</div>
  <ul class="contact-list">
    <li>010 555 0188</li>
    <li>010 555 0199</li>
    <li>hello@haloware.com</li>
    <li>www.haloware.com</li>
    <li>12 Harbor Lane, Westfield 4021</li>
  </ul>
  <div class="letter">
    <p>July 2, 2012</p>
    <p><strong>Dear CH,</strong><br>12 Harbor Lane, Westfield</p>
    <p>is simply dummy text of the printing and typesetting industry. Lorem Ipsum has been the industry's standard dummy text ever since the 1500s, when an unknown printer took a galley of type and scrambled it to make a type specimen book. It has survived not only five centuries, but also the leap into electronic typesetting, remaining essentially unchanged. It was popularised in the 1960s with the release of transfer sheets containing Lorem Ipsum passages, and more recently with modern layout software including versions of Lorem Ipsum.</p>
    <p class="gap">is simply dummy text of the printing and typesetting industry. Lorem Ipsum has been the industry's standard dummy text ever since the 1500s, when an unknown printer took a galley of type and scrambled it to make</p>
    <p>is simply dummy text of the printing and typesetting industry. Lorem Ipsum has been the industry's standard dummy text ever since the 1500s, when an unknown printer took a galley of type and scrambled it to make a type specimen book. It has survived not only five centuries, but also the leap into electronic typesetting, remaining essentially unchanged. It was popularised in the 1960s with the release of transfer sheets containing Lorem Ipsum passages, and more recently with modern layout software including versions of Lorem Ipsum.</p>
    <p>Best Regards,</p>
    <div class="signature-line"></div>
    <p><strong>Daniel Reyes</strong><br>Director<br><br>12 Harbor Lane, Westfield</p>
  </div>
  <div class="band" role="img" aria-label="Decorative wave band in dark grey and light blue"></div>
</section>

<section class="piece folder">
  <div class="brand"><span class="brand-dot"></span>Haloware</div>
  <div class="band" role="img" aria-label="Decorative wave band in dark grey and light blue"></div>
  <div class="site">www.haloware.com</div>
</section>

<section class="piece card card-front">
  <div class="brand"><span class="brand-dot"></span>Haloware</div>
  <div class="holder"><div class="name">Marcus Hale</div><div>Managing Director</div></div>
  <div class="band" role="img" aria-label="Decorative wave band in dark grey and light blue"></div>
  <ul class="card-contacts">
    <li>010 555 0188</li>
    <li>010 555 0199</li>
    <li>hello@haloware.com</li>
    <li>www.haloware.com</li>
    <li>12 Harbor Lane, Westfield 4021</li>
  </ul>
</section>

<section class="piece card card-back">
  <div class="brand"><span class="brand-dot"></span>Haloware</div>
</section>

<section class="piece envelope-front">
  <div class="brand"><span class="brand-dot"></span>Haloware</div>
  <div class="band" role="img" aria-label="Decorative wave band in dark grey and light blue"></div>
  <div class="site">www.haloware.com</div>
</section>

<section class="piece envelope-back">
  <div class="flap"></div>
  <div class="site">www.haloware.com</div>
</section>

</body>
</html>
```